Private Practice Dietitian's Business Card

A 2-sided business card for a dietitian (medical nutritionist) in private practice within a natural therapies allied health clinic. The business card needs to imply warmth and professionalism.
Target Market(s)
Doctors who may refer patients to a dietitian and patients themselves who may request dietetic assessment, education and counselling.
Industry/Entity Type
Business
Requirements
Must have
- The business card must be an intense blue on the front at the bottom, gradually lightening towards the top of the card. Please see:
http://example-pinboard.net/remy_hastwell/card-ideas/
for an example from "The quiet of the orchard" book. I'd like an apple tree on the left with a pale silver/grey trunk (like the silver in the book cover)and branches that bends over to the right above the writing. Apples to be a turquoise/aqua colour similar to that in "The quiet of the orchard" book cover. Front cover writing to read:
plateplan
0482 913 276
plateplan@kettlemail.net.au
'plateplan' is one word but I would like the 'my' in turquoise/aqua to match the apples and the 'dietitian' and the phone number and email address in the pale silver/grey to match the tree trunk.
I'd like the plateplan in larger font than the phone number and email address but for all 3 lines of text on the front of the business card to be stretched so they have the same left and right margin. (I hope this makes sense!)
I would like the back of the card to be white and the top section of text to be in the same turquoise/aqua from the apples on the front of the card and to read:
MAREE TOLBIN
Accredited Practising Dietitian (APD)
Bachelor of Health Science (Nutrition & Dietetics) - Honours
Master of Nutrition & Dietetics
This text should be stretched/compacted so that it all has the same left and right margin.
After this text there should be a blank line for spacing before the next section of text, which is to be in the silver/grey of the tree trunk. It should read:
Weight management
Diabetes
Impaired fasting glycaemia
Impaired glucose tolerance
Gestational diabetes
Wellness & general nutrition
Cardiovascular disease
high blood pressure
High cholesterol
High triglycerides
Fatty liver
Constipation
Diverticular disease
Coeliac disease
Irritable bowel syndrome
Gastroesophageal reflux
Lactose intolerance
Gout
Polycystic ovarian syndrome
Fertility
Pregnancy
Breastfeeding
Osteoporosis
Iron deficiency
Vegetarian eating
This set of text can run across the page from left to right and each medical condition could be separated from the next in some way to help with ease of reading. For example perhaps a space, dot and another space could separate the medical conditions. This set of text should be stretched so that the left and right margins of each line is the same. Thank you!
Nice to have
- An easy-to read but 'elegant' font would be nice - but I have no idea which one! Nothing too ornate, but not dull standard Times New Roman/Arial/Comic Sans either!
Should not have
- Times new roman/comic sans/arial fonts

```html
<!DOCTYPE html>
<html lang="en">
<head>
<meta charset="utf-8">
<title>plateplan – business card, front and back</title>
<link rel="stylesheet" href="https://fonts.googleapis.com/css2?family=Alegreya:ital,wght@1,400&family=Lobster&display=swap">
<style>
  :root {
    --paper: #ffffff;
    --aqua: #1ba3ad;
    --aqua-deep: #4cc3d3;
    --aqua-pale: #eaf8fa;
    --silver: #f2f4f3;
    --silver-shade: #dfe4e3;
    --grey-text: #9b9b9b;
    --ink: #111111;
    --crop: #333333;
  }
  * { margin: 0; padding: 0; box-sizing: border-box; }
  html, body { width: 1200px; height: 848px; overflow: hidden; background: var(--paper); }
  .sheet { position: relative; width: 1200px; height: 848px; }

  .crop-marks { position: absolute; inset: 0; }

  /* ---------- front ---------- */
  .card-front {
    position: absolute; left: 108px; top: 53px; width: 477px; height: 310px;
    background: linear-gradient(200deg, var(--aqua-pale) 0%, #b9e7ee 35%, #82d5e1 70%, var(--aqua-deep) 100%);
    overflow: hidden;
  }
  .tree-art {
    position: absolute; left: 0; top: 18px; width: 215px; height: 292px;
    border-radius: 0 110px 0 0;
    background: linear-gradient(90deg, rgba(242,244,243,0.92) 0%, rgba(223,228,227,0.75) 55%, rgba(242,244,243,0.45) 100%);
  }
  .front-text { position: absolute; left: 149px; top: 146px; width: 300px; color: var(--silver); }
  .wordmark {
    font-family: "Lobster", cursive; font-weight: 400; font-size: 66px; line-height: 66px;
    text-align: center; letter-spacing: 2px; color: var(--silver); white-space: nowrap;
  }
  .dotted { border-top: 2px dotted currentColor; height: 0; }
  .front-text .dotted { margin-top: 12px; color: var(--silver); }
  .phone, .email {
    font-family: "Alegreya", serif; font-style: italic; white-space: nowrap;
  }
  .phone { font-size: 25px; line-height: 28px; margin-top: 2px; letter-spacing: 14.5px; text-align: justify; text-align-last: justify; margin-right: -14px; }
  .email { font-size: 17px; line-height: 20px; letter-spacing: 4.3px; margin-bottom: 6px; }

  /* ---------- back ---------- */
  .card-back { position: absolute; left: 108px; top: 465px; width: 477px; height: 325px; background: var(--paper); }
  .back-text { position: absolute; left: 24px; top: 18px; width: 430px; }
  .credentials { color: var(--aqua); font-family: "Alegreya", serif; font-style: italic; font-size: 18.5px; }
  .credentials .line { line-height: 29px; text-align: justify; text-align-last: justify; white-space: nowrap; }
  .practitioner { font-family: "Lobster", cursive; font-style: normal; font-size: 32px; letter-spacing: 0.5px; }
  .back-text .dotted { color: var(--aqua); margin: 10px 0 8px; border-top-width: 3px; }
  .services { color: var(--grey-text); font-family: "Alegreya", serif; font-style: italic; font-size: 19.5px; letter-spacing: 1.5px; }
  .services .line { line-height: 29px; text-align: justify; text-align-last: justify; white-space: nowrap; }

  .label { position: absolute; font-family: "Lobster", cursive; font-size: 12px; color: var(--ink); }
  .label-front { left: 305px; top: 402px; }
  .label-back { left: 318px; top: 816px; }
</style>
</head>
<body>
<main class="sheet">
  <svg class="crop-marks" width="1200" height="848" viewBox="0 0 1200 848" aria-hidden="true">
    <g stroke="var(--crop)" stroke-width="1">
      <line x1="106" y1="38" x2="106" y2="52"/><line x1="92" y1="52" x2="106" y2="52"/>
      <line x1="586" y1="38" x2="586" y2="52"/><line x1="586" y1="52" x2="600" y2="52"/>
      <line x1="106" y1="364" x2="106" y2="378"/><line x1="92" y1="364" x2="106" y2="364"/>
      <line x1="586" y1="364" x2="586" y2="378"/><line x1="586" y1="364" x2="600" y2="364"/>
      <line x1="106" y1="454" x2="106" y2="468"/><line x1="92" y1="468" x2="106" y2="468"/>
      <line x1="586" y1="454" x2="586" y2="468"/><line x1="586" y1="468" x2="600" y2="468"/>
      <line x1="106" y1="780" x2="106" y2="794"/><line x1="92" y1="780" x2="106" y2="780"/>
      <line x1="586" y1="780" x2="586" y2="794"/><line x1="586" y1="780" x2="600" y2="780"/>
    </g>
  </svg>

  <section class="card-front" aria-label="Front of card">
    <div class="tree-art" role="img" aria-label="Illustration of a pale silver apple tree with aqua apples, branches arching to the right over the text"></div>
    <div class="front-text">
      <h1 class="wordmark">plateplan</h1>
      <div class="dotted"></div>
      <p class="phone">0482 913 276</p>
      <p class="email">plateplan@kettlemail.net.au</p>
      <div class="dotted"></div>
    </div>
  </section>
  <p class="label label-front">front of card</p>

  <section class="card-back" aria-label="Back of card">
    <div class="back-text">
      <div class="credentials">
        <p class="line"><span class="practitioner">Maree&nbsp;Tolbin</span> ~ Accredited Practising</p>
        <p class="line">Dietitian (APD) ~ Bachelor of Health Science (Nutrition</p>
        <p class="line">&amp; Dietetics) ~ Honours Master of Nutrition &amp; Dietetics</p>
      </div>
      <div class="dotted"></div>
      <div class="services">
        <p class="line">Weight management ~ Diabetes ~ Impaired fasting</p>
        <p class="line">glycaemia ~ Impaired glucose tolerance ~</p>
        <p class="line">Gestational diabetes ~ Wellness &amp; general</p>
        <p class="line">nutrition ~ Cardiovascular disease ~ High blood</p>
        <p class="line">pressure ~ High cholesterol ~ High triglycerides</p>
      </div>
    </div>
  </section>
  <p class="label label-back">back of card</p>
</main>
</body>
</html>
```